New UI for electricity data tool

We are looking for a new UI for the website http://vantorgrid.net. Reassessing the structure of the website is as important as specific design choices. We have created a uniquely comprehensive set of global electricity generation data and now we are looking for creative solutions for how to make this data accessible. Researching and referencing other similar projects may be a good idea.

Goals:
• The website should clearly communicate the most important general conclusions that can be drawn from the data, including:
◦ The world as a whole is not moving away from fossil fuels for electricity generation
◦ There are substantial differences between regions
▪ Some regions have basically solved the problem – they already generate almost all of their electricity from non-fossil sources
▪ Some regions have greatly improved in terms of decarbonizing their electricity generation.
▪ Some regions have greatly deteriorated, in other words they are using a much higher share of fossil fuels to generate their electricity.
◦ There are substantial differences between energy sources. Regions that have successfully decarbonized their electricity generation have usually done so using hydro and/or nuclear. Other low-carbon energy sources have grown quickly in relative terms in the last few years but are so far contributing little in absolute numbers.
• The website should serve as inspiration for energy policy debates. The goal is to study the impact of existing policies around the world. Energy policy here refers to particular combinations of energy sources – ie how much have the countries invested in each type of electricity generation. The tool should help answer questions such as:
◦ Which countries have done the most in terms of decarbonizing their electricity generation?
◦ Which types of energy polices have lead to the fastest decarbonization processes around the world?
◦ If country A changed its energy policy to be more like country B, what would the likely impact be?

Challenges:
• There is a lot of data – it can be overwhelming to the user. It’s crucial to make the site easy to navigate. The main page should highlight the most important data, and it should also be straightforward to find more detailed data.
• Data availability varies from region to region. The current interface addresses this with the default option “Exclude regions with limited data”. We expect a better approach to dealing with this issue. For some regions and years energy sources are grouped together as for example “other renewables” whereas in other cases more detailed data is available.
• Credibility is crucial. Our data is based on a combination of data from KQ and the Tessary Trust. It must be very clear throughout the site where each data set comes from.

Details:
• The current chart color schemes is loosely based on the carbon emissions from each energy source. This should not necessarily be so. The goal is to on the one hand communicate clearly the amounts of fossil vs non-fossil energy that are generated by each region. At the same time we also want to make it easy to view specific energy sources.

Inspirational websites:
• https://www.grafmelo.org/
• https://trendquarrily.org/

Let's simplify. The main metric to focus on is Brisavolt Index and the extent to which the world and each country has achieved it (eg Iceland 100%, France 88% and so on). I'm considering changing the name of the site to BrisavoltIndex.org. We can use maps, charts and perhaps other tools to communicate this main message. What's the best way of doing this?

```html
<!DOCTYPE html>
<html lang="en">
<head>
<meta charset="utf-8">
<title>Vantorgrid.net – Regions</title>
<link href="https://fonts.googleapis.com/css2?family=Roboto:wght@400;500;700&display=swap" rel="stylesheet">
<style>
:root{
  --navy:#384557;
  --navy-dark:#37455a;
  --page:#efefef;
  --white:#ffffff;
  --teal:#0aa8b8;
  --lime:#96c60a;
  --grey-bar:#a6a6a6;
  --grey-light:#c8c8c8;
  --text:#333a44;
  --muted:#6b6f75;
  --line:#c9ccd1;
}
*{box-sizing:border-box;margin:0;padding:0}
html,body{width:1200px;height:842px;overflow:hidden}
body{font-family:'Roboto',sans-serif;background:var(--page);color:var(--text);position:relative}
a{color:inherit;text-decoration:none}

.site-header{position:absolute;left:0;top:0;width:1200px;height:69px;background:var(--navy)}
.brand{position:absolute;font-weight:700;color:var(--white);letter-spacing:.2px}
.site-header .brand{left:79px;top:14px;font-size:29px}
.main-nav a{position:absolute;top:24px;font-size:14.5px;color:var(--white)}
.main-nav .is-active{color:var(--lime);border-bottom:1px solid var(--lime);padding-bottom:2px}
.search{position:absolute;left:820px;top:16px;width:300px;height:37px;border:1px solid #c0c6cf;border-radius:19px;color:var(--white);font-size:14.5px;padding:9px 0 0 15px}
.search svg{position:absolute;right:13px;top:9px}

.filter-bar{position:absolute;left:0;top:69px;width:1200px;height:82px;background:var(--white);box-shadow:0 1px 2px rgba(0,0,0,.05)}
.filter{position:absolute;top:23px;height:33px;border:1px solid var(--line);border-radius:17px;font-size:12px;color:var(--text);padding:9px 0 0 9px}
.filter.placeholder{color:var(--muted)}
.filter .caret{position:absolute;right:10px;top:14px;width:0;height:0;border-left:3.5px solid transparent;border-right:3.5px solid transparent;border-top:4px solid #222}

.chart-card{position:absolute;left:124px;top:194px;width:682px;height:348px;background:var(--white);border-radius:3px;box-shadow:0 1px 3px rgba(0,0,0,.08)}
.chart-card svg{position:absolute;left:0;top:0}
.axis-label{font-size:11.5px;fill:var(--text)}
.legend-label{font-size:11px;fill:var(--text)}

.region-summary{position:absolute;left:854px;top:240px;width:230px}
.region-summary h1{font-size:24px;font-weight:700;color:var(--navy);letter-spacing:.5px}
.region-summary p{margin-top:9px;font-size:14px;line-height:24px;color:var(--text)}
.region-summary p a{color:var(--teal);text-decoration:underline}
.source-btn{position:absolute;left:0;width:127px;height:34px;border-radius:17px;color:var(--white);font-weight:500;font-size:14px;text-align:center;line-height:34px}
.source-btn.tessary{top:149px;background:var(--teal)}
.source-btn.kq{top:193px;background:var(--lime)}

.pagination a{position:absolute;top:602px;height:19px;min-width:22px;background:var(--white);border:1px solid #dcdcdc;border-radius:2px;font-size:11px;font-weight:500;text-align:center;line-height:17px;color:var(--text)}
.pagination .next{border:none;background:none;font-size:9px;letter-spacing:.5px;left:335px}

.site-footer{position:absolute;left:0;top:651px;width:1200px;height:191px;background:var(--navy)}
.site-footer .brand{left:171px;top:48px;font-size:29px}
.footer-nav a{position:absolute;top:98px;font-size:14.5px;color:var(--white)}
.copyright{position:absolute;left:167px;top:136px;font-size:12px;color:var(--white)}
.social{position:absolute;top:85px;width:39px;height:39px;border:2px solid var(--white);border-radius:50%}
</style>
</head>
<body>

<header class="site-header">
  <a class="brand" href="#">Vantorgrid.net</a>
  <nav class="main-nav">
    <a class="is-active" href="#" style="left:365px">Regions</a>
    <a href="#" style="left:455px">Energy Sources</a>
    <a href="#" style="left:592px">Changes</a>
    <a href="#" style="left:690px">Data Sources</a>
  </nav>
  <div class="search">Search
    <svg width="19" height="19" viewBox="0 0 19 19" aria-hidden="true"><circle cx="8" cy="8" r="6.5" fill="none" stroke="#fff" stroke-width="2"/><line x1="12.8" y1="12.8" x2="17.5" y2="17.5" stroke="#fff" stroke-width="2.2" stroke-linecap="round"/></svg>
  </div>
</header>

<section class="filter-bar">
  <div class="filter placeholder" style="left:172px;width:190px">Select Regions</div>
  <div class="filter" style="left:374px;width:213px">Sort by low-carbon(%)<span class="caret"></span></div>
  <div class="filter" style="left:596px;width:138px">Show %<span class="caret"></span></div>
  <div class="filter" style="left:743px;width:281px">Exclude regions with limitd data<span class="caret"></span></div>
</section>

<section class="chart-card">
  <svg width="682" height="348" viewBox="0 0 682 348" role="img" aria-label="Stacked bar chart of Kenya electricity sources, 1971 to 1979">
    <g stroke="#e6e6e6" stroke-width="1">
      <line x1="43" y1="34" x2="502" y2="34"/><line x1="43" y1="57.9" x2="502" y2="57.9"/>
      <line x1="43" y1="81.8" x2="502" y2="81.8"/><line x1="43" y1="105.7" x2="502" y2="105.7"/>
      <line x1="43" y1="129.6" x2="502" y2="129.6"/><line x1="43" y1="153.5" x2="502" y2="153.5"/>
      <line x1="43" y1="177.4" x2="502" y2="177.4"/><line x1="43" y1="201.3" x2="502" y2="201.3"/>
      <line x1="43" y1="225.2" x2="502" y2="225.2"/><line x1="43" y1="249.1" x2="502" y2="249.1"/>
      <line x1="43" y1="273" x2="502" y2="273"/>
    </g>
    <line x1="43" y1="30" x2="43" y2="273" stroke="#cfcfcf"/>
    <g class="axis-label" text-anchor="end">
      <text x="35" y="38">100</text><text x="35" y="62">90</text><text x="35" y="86">80</text>
      <text x="35" y="110">70</text><text x="35" y="134">60</text><text x="35" y="158">50</text>
      <text x="35" y="182">40</text><text x="35" y="206">30</text><text x="35" y="229">20</text>
      <text x="35" y="253">10</text><text x="35" y="277">0</text>
    </g>

    <g class="bar">
      <rect x="59" y="34" width="22" height="95.6" fill="var(--grey-bar)"/>
      <rect x="59" y="129.6" width="22" height="7.2" fill="var(--lime)"/>
      <rect x="59" y="136.8" width="22" height="31" fill="var(--teal)"/>
      <rect x="59" y="167.8" width="22" height="105.2" fill="var(--navy)"/>
    </g>
    <g class="bar">
      <rect x="109" y="34" width="22" height="93.2" fill="var(--grey-bar)"/>
      <rect x="109" y="127.2" width="22" height="7.2" fill="var(--lime)"/>
      <rect x="109" y="134.4" width="22" height="28.7" fill="var(--teal)"/>
      <rect x="109" y="163.1" width="22" height="109.9" fill="var(--navy)"/>
    </g>
    <g class="bar">
      <rect x="163" y="34" width="22" height="105.2" fill="var(--grey-bar)"/>
      <rect x="163" y="139.2" width="22" height="9.5" fill="var(--lime)"/>
      <rect x="163" y="148.7" width="22" height="23.9" fill="var(--teal)"/>
      <rect x="163" y="172.6" width="22" height="100.4" fill="var(--navy)"/>
    </g>
    <g class="bar">
      <rect x="214" y="34" width="22" height="71.7" fill="var(--grey-bar)"/>
      <rect x="214" y="105.7" width="22" height="9.6" fill="var(--lime)"/>
      <rect x="214" y="115.3" width="22" height="23.9" fill="var(--teal)"/>
      <rect x="214" y="139.2" width="22" height="133.8" fill="var(--navy)"/>
    </g>
    <g class="bar">
      <rect x="265" y="34" width="22" height="71.7" fill="var(--grey-light)"/>
      <rect x="265" y="105.7" width="22" height="7.2" fill="var(--lime)"/>
      <rect x="265" y="112.9" width="22" height="23.9" fill="var(--teal)"/>
      <rect x="265" y="136.8" width="22" height="136.2" fill="var(--navy)"/>
    </g>
    <g class="bar">
      <rect x="315" y="34" width="22" height="105.2" fill="var(--grey-bar)"/>
      <rect x="315" y="139.2" width="22" height="9.5" fill="var(--lime)"/>
      <rect x="315" y="148.7" width="22" height="23.9" fill="var(--teal)"/>
      <rect x="315" y="172.6" width="22" height="100.4" fill="var(--navy)"/>
    </g>
    <g class="bar">
      <rect x="366" y="34" width="22" height="105.2" fill="var(--grey-bar)"/>
      <rect x="366" y="139.2" width="22" height="9.5" fill="var(--lime)"/>
      <rect x="366" y="148.7" width="22" height="23.9" fill="var(--teal)"/>
      <rect x="366" y="172.6" width="22" height="100.4" fill="var(--navy)"/>
    </g>
    <g class="bar">
      <rect x="416" y="34" width="22" height="47.8" fill="var(--grey-bar)"/>
      <rect x="416" y="81.8" width="22" height="7.2" fill="var(--lime)"/>
      <rect x="416" y="89" width="22" height="23.9" fill="var(--teal)"/>
      <rect x="416" y="112.9" width="22" height="160.1" fill="var(--navy)"/>
    </g>
    <g class="bar">
      <rect x="469" y="34" width="22" height="31.1" fill="var(--grey-bar)"/>
      <rect x="469" y="65.1" width="22" height="7.1" fill="var(--lime)"/>
      <rect x="469" y="72.2" width="22" height="23.9" fill="var(--teal)"/>
      <rect x="469" y="96.1" width="22" height="176.9" fill="var(--navy)"/>
    </g>

    <g class="axis-label" text-anchor="middle">
      <text x="70" y="293">1971</text><text x="120" y="293">1972</text><text x="174" y="293">1973</text>
      <text x="225" y="293">1974</text><text x="276" y="293">1975</text><text x="326" y="293">1976</text>
      <text x="377" y="293">1977</text><text x="427" y="293">1978</text><text x="480" y="293">1979</text>
    </g>

    <rect x="41" y="320" width="455" height="4" rx="2" fill="#efefef"/>
    <rect x="41" y="320" width="52" height="4" rx="2" fill="#cfcfcf"/>

    <g class="legend">
      <circle cx="525.5" cy="137" r="3.5" fill="var(--lime)"/><text class="legend-label" x="533" y="141">Non-fossil</text>
      <circle cx="525.5" cy="151" r="3.5" fill="var(--navy)"/><text class="legend-label" x="533" y="155">Hydro</text>
      <circle cx="525.5" cy="165" r="3.5" fill="var(--teal)"/><text class="legend-label" x="533" y="169">Renewables-except-hydro</text>
      <circle cx="525.5" cy="179" r="3.5" fill="var(--grey-bar)"/><text class="legend-label" x="533" y="183">oil</text>
    </g>
  </svg>
</section>

<aside class="region-summary">
  <h1>KENYA</h1>
  <p>88% of the electricity in Kenya is generated from <a href="#">Brisavolt Index.</a> The primary low-carbon power source is hydro.</p>
  <a class="source-btn tessary" href="#">Tessary Trust</a>
  <a class="source-btn kq" href="#">KQ</a>
</aside>

<nav class="pagination">
  <a href="#" style="left:172px">1</a>
  <a href="#" style="left:203px">2</a>
  <a href="#" style="left:234px">3</a>
  <a href="#" style="left:265px;min-width:25px">...</a>
  <a href="#" style="left:298px">6</a>
  <a class="next" href="#">NEXT</a>
</nav>

<footer class="site-footer">
  <a class="brand" href="#">Vantorgrid.net</a>
  <nav class="footer-nav">
    <a href="#" style="left:170px">Regions</a>
    <a href="#" style="left:259px">Energy Sources</a>
    <a href="#" style="left:396px">Changes</a>
    <a href="#" style="left:494px">Data Sources</a>
  </nav>
  <p class="copyright">© 2020 Vantorgrid.net. All rights reserved.</p>
  <a class="social" href="#" aria-label="Social link 1" style="left:841px"></a>
  <a class="social" href="#" aria-label="Social link 2" style="left:888px"></a>
  <a class="social" href="#" aria-label="Social link 3" style="left:937px"></a>
  <a class="social" href="#" aria-label="Social link 4" style="left:985px"></a>
</footer>

</body>
</html>
```